Design a DL flyer double sided 4 colour 210mm x 95 mm (portrait) for the launch of a new yoga studio opening in North Melbourne on the 23 November 2013.
The final design should communicate with a strong call to action- the opening date , register to receive your first class free and like us on Chatterbox.
The studio provides a tranquil, open space to practice yoga, create a feeling of light, peace and a nurturing environment, please create this feeling in the design.

An example design mock (rough design feel free to move around as required, includes final content) print specifications, logo, typography style and image attached.
The reverse side to include logo, address and please design the timetable for the launch week (refer design mock)
Have also attached a reverse logo for a dark background and are open to designer providing examples with various background colours and effects.
Back content can be moved to the front side if required to facilitate design

Target Market(s)

People in the area who are practicing yoga elsewhere and encourage them to come to the studio to try us out with a free opening offer in our first week. And people new to yoga wanting to give it a try.
Experienced yoga people and people new to yoga - all ages

Industry/Entity Type

Environment

Requirements
Must have
• The Lotus Nook logo physical address, website address, the tagline live, breathe, love...
The final design should communicate with a strong call to action- the opening date , register to receive your first class free and like us on Chatterbox. and the website address thelotusnook.com.au, drive them to the website to register.
The studio provides a tranquil, open space to practice yoga, create a feeling of light, peace and a nurturing environment, please create this feeling in the design

```html
<!DOCTYPE html>
<html lang="en">
<head>
<meta charset="utf-8">
<title>The Lotus Nook – Opening Flyer</title>
<link href="https://fonts.googleapis.com/css2?family=Open+Sans:ital,wght@0,400;0,600;0,700;1,400&display=swap" rel="stylesheet">
<style>
  :root {
    --page: #ffffff;
    --panel: #000000;
    --accent: #f5a330;
    --ink: #ffffff;
    --rule-v: #d9d9d9;
    --rule-h: #8a8a8a;
    --leaf-light: #8fb46a;
    --leaf-dark: #2f4d22;
  }
  * { box-sizing: border-box; margin: 0; padding: 0; }
  html, body { width: 1200px; height: 1000px; overflow: hidden; background: var(--page); }
  body { position: relative; font-family: "Open Sans", sans-serif; color: var(--ink); }

  .flyer-side { position: absolute; top: 0; width: 452px; height: 1000px; background: var(--panel); text-align: center; }
  .flyer-front { left: 118px; }
  .flyer-back { left: 627px; }

  .brand { position: absolute; left: 0; right: 0; display: flex; justify-content: center; align-items: center; color: var(--accent); font-weight: 600; }
  .brand-dot { background: var(--accent); border-radius: 50%; }
  .brand-front { top: 62px; font-size: 44px; gap: 14px; }
  .brand-front .brand-dot { width: 38px; height: 38px; }
  .brand-back { top: 786px; font-size: 19px; gap: 7px; }
  .brand-back .brand-dot { width: 18px; height: 18px; }

  .tagline { position: absolute; top: 176px; left: 0; right: 0; font-style: italic; font-size: 22px; }
  .hero-photo { position: absolute; left: 130px; top: 210px; width: 192px; height: 212px;
    background: linear-gradient(180deg, var(--leaf-light) 0%, #5f8a45 45%, var(--leaf-dark) 80%, #6a7f7a 100%); }

  .opening-label { position: absolute; top: 454px; left: 0; right: 0; color: var(--accent); font-size: 18px; }
  .opening-date { position: absolute; top: 486px; left: 0; right: 0; font-size: 70px; font-weight: 700; letter-spacing: -1px; line-height: 1; }
  .address { position: absolute; top: 578px; left: 0; right: 0; font-size: 33px; line-height: 36px; }

  .offer { position: absolute; left: 0; right: 0; }
  .star { display: block; color: var(--accent); font-weight: 700; font-size: 30px; line-height: 22px; height: 22px; }
  .offer-free { top: 716px; font-size: 27px; line-height: 29px; }
  .offer-free em { font-style: normal; color: var(--accent); }
  .offer-week { top: 814px; font-size: 21px; line-height: 22px; }
  .offer-book { top: 902px; font-size: 20px; line-height: 22px; }

  .about { position: absolute; top: 56px; left: 0; right: 0; font-size: 20.5px; line-height: 28.5px; }

  .times-title { position: absolute; top: 526px; left: 0; right: 0; color: var(--accent); font-size: 18px; }
  .timetable { position: absolute; left: 29px; top: 565px; width: 393px; border-collapse: collapse; table-layout: fixed; }
  .timetable th { background: var(--accent); color: var(--ink); font-weight: 400; font-size: 17px; height: 23px; line-height: 23px; border-right: 1px solid var(--rule-v); }
  .timetable td { font-size: 11px; height: 22.5px; border-right: 1px solid var(--rule-v); border-bottom: 1px solid var(--rule-h); }
  .timetable th:last-child, .timetable td:last-child { border-right: none; }
  .timetable col.weekend { width: 55px; }

  .contact { position: absolute; top: 832px; left: 0; right: 0; font-size: 14px; line-height: 17px; }
  .contact dt { color: var(--accent); }
  .contact dd { margin-bottom: 16px; }
</style>
</head>
<body>

<section class="flyer-side flyer-front">
  <div class="brand brand-front"><span class="brand-dot"></span><span>The Lotus Nook</span></div>
  <p class="tagline">live, breathe, love…</p>
  <div class="hero-photo" role="img" aria-label="Photo of a woman meditating cross-legged in white clothing, green forest behind and water reflection below"></div>
  <p class="opening-label">NEW YOGA STUDIO OPENING</p>
  <p class="opening-date">23.11.2013</p>
  <p class="address">47 Harrow Street<br>North Melbourne</p>
  <p class="offer offer-free"><span class="star">*</span>First class <em>FREE</em><br>in opening week</p>
  <p class="offer offer-week"><span class="star">*</span>Opening week<br>23 Nov – 29 Nov inclusive</p>
  <p class="offer offer-book"><span class="star">*</span>To book your free class go online to<br>register and book, like us on Chatterbox</p>
</section>

<section class="flyer-side flyer-back">
  <p class="about">A generously sized natural studio in<br>North Melbourne, providing dynamic<br>flow vinyasa and restorative yoga for<br>all levels from newbies to experienced,<br>with a collection of the best teachers.<br>Embark on a journey to happiness<br>within yourself – be healthy in your<br>body and mind.<br>Science is finally proving what yogis<br>have known all along.... yoga is good<br>for you!<br>A tranquil space to de stress, build<br>strength and healing in our bodies<br>through our own tapas (internal heat).</p>

  <p class="times-title">CLASS TIMES</p>
  <table class="timetable">
    <colgroup><col class="weekend"><col class="weekend"><col><col><col><col><col></colgroup>
    <thead><tr><th>sat</th><th>sun</th><th>mon</th><th>tue</th><th>wed</th><th>thu</th><th>fri</th></tr></thead>
    <tbody>
      <tr><td>9.00 am</td><td>9.00 am</td><td>6.30 am</td><td>6.30 am</td><td>6.30 am</td><td>6.30 am</td><td>6.30 am</td></tr>
      <tr><td>10.30 am</td><td>10.30 am</td><td>9.30 am</td><td>9.30 am</td><td>9.30 am</td><td>9.30 am</td><td>9.30 am</td></tr>
      <tr><td>4.00 pm</td><td>4.00 pm</td><td>12.30 pm</td><td>12.30 pm</td><td>12.30 pm</td><td>12.30 pm</td><td>12.30 am</td></tr>
      <tr><td></td><td></td><td>5.30 pm</td><td>5.30 pm</td><td>5.30 pm</td><td>5.30 pm</td><td>5.30 pm</td></tr>
      <tr><td style="border-bottom:none"></td><td style="border-bottom:none"></td><td style="border-bottom:none">7.00pm</td><td style="border-bottom:none">7.00pm</td><td style="border-bottom:none">7.00pm</td><td style="border-bottom:none">7.00pm</td><td style="border-bottom:none">7.00pm</td></tr>
    </tbody>
  </table>

  <div class="brand brand-back"><span class="brand-dot"></span><span>The Lotus Nook</span></div>
  <dl class="contact">
    <dt>website</dt><dd>www.thelotusnook.com.au</dd>
    <dt>chatterbox</dt><dd>thelotusnook</dd>
    <dt>telephone</dt><dd>0491-570156</dd>
  </dl>
</section>

</body>
</html>
```